brightmesh Business Card

Already have the logo, but now need the business card design

Industry/Entity Type

Business Software

Contact Information for Business Card

web site will be brightmesh.io / The card should have the person name / position / mobile / email / and company address

Colors

Designer to choose colors to be used in the design.

Requirements
Must have
• See business card details
• One side to have the brightmesh logo
Nice to have
• If possible the 'O' from flow can be watermarked into the second side
• Try to fit in the words brightmesh Business Solutions

```html
<!DOCTYPE html>
<html lang="en">
<head>
<meta charset="utf-8">
<title>brightmesh Business Card</title>
<link href="https://fonts.googleapis.com/css2?family=Lato:wght@400;700&display=swap" rel="stylesheet">
<style>
  :root {
    --page-bg: #2a2a2c;
    --card-front: #1d1e20;
    --card-back: #6b6b6b;
    --card-back-light: #767676;
    --text-grey: #8a8a8a;
    --text-soft: #9a9a9a;
    --accent-red: #e0202a;
    --white: #ffffff;
    --rule: #4a4a4c;
  }
  * { box-sizing: border-box; margin: 0; padding: 0; }
  html, body { width: 1200px; height: 1108px; overflow: hidden; }
  body {
    background: var(--page-bg);
    font-family: "Lato", Arial, sans-serif;
    position: relative;
  }
  .card {
    position: absolute;
    top: 214px;
    width: 400px;
    height: 680px;
    border-radius: 26px;
    overflow: hidden;
  }
  .card-front { left: 160px; background: var(--card-front); }
  .card-back { left: 640px; background: var(--card-back); }

  .front-brand { position: absolute; top: 120px; left: 0; right: 0; text-align: center; }
  .brand-name {
    font-size: 64px; font-weight: 400; color: var(--text-grey);
    letter-spacing: -1px; line-height: 1;
  }
  .brand-tagline {
    margin-top: 6px; font-size: 25px; font-weight: 700;
    color: var(--text-grey); letter-spacing: 0.5px;
  }

  .person { position: absolute; top: 330px; left: 0; right: 0; text-align: center; }
  .person-name { font-size: 24px; font-weight: 700; color: var(--text-grey); letter-spacing: 0.5px; }
  .person-name .surname { color: var(--accent-red); }
  .person-role { margin-top: 4px; font-size: 18px; color: var(--text-soft); }

  .contact-icons {
    position: absolute; top: 408px; left: 60px; right: 60px;
    display: flex; align-items: center; gap: 6px;
  }
  .contact-icons .rule { flex: 1; height: 1px; background: var(--rule); }
  .contact-icons svg { width: 24px; height: 24px; }

  .contact-list {
    position: absolute; top: 452px; left: 0; right: 0;
    text-align: center; font-size: 19px; line-height: 28px; color: var(--text-soft);
  }
  .divider { position: absolute; top: 548px; left: 90px; right: 90px; height: 1px; background: var(--rule); }
  .address {
    position: absolute; top: 564px; left: 0; right: 0;
    text-align: center; font-size: 19px; line-height: 28px; color: var(--text-soft);
  }

  .back-pattern {
    position: absolute; inset: 0;
    background: linear-gradient(180deg, var(--card-back-light) 0%, var(--card-back) 70%);
  }
  .back-brand {
    position: absolute; left: 0; right: 0; bottom: 110px;
    text-align: center; font-size: 68px; font-weight: 400;
    color: var(--white); letter-spacing: -1px; line-height: 1;
  }
</style>
</head>
<body>
  <section class="card card-front">
    <div class="front-brand">
      <div class="brand-name">brightmesh</div>
      <div class="brand-tagline">BUSINESS SOLUTIONS</div>
    </div>

    <div class="person">
      <div class="person-name">DANIEL <span class="surname">CARTER</span></div>
      <div class="person-role">Managing Director</div>
    </div>

    <div class="contact-icons">
      <span class="rule"></span>
      <svg viewBox="0 0 24 24" aria-label="Phone">
        <circle cx="12" cy="12" r="12" fill="#6a6a6a"/>
        <path d="M8 7c1-1 2 0 2.5 1l.5 1.5c0 .8-.8 1.2-.8 1.6.5 1.3 1.5 2.3 2.7 2.8.4 0 .8-.8 1.6-.8l1.5.5c1 .5 2 1.5 1 2.5-2 2-8-2-9.5-4.5C6.8 9.8 7 8 8 7z" fill="#1d1e20"/>
      </svg>
      <svg viewBox="0 0 24 24" aria-label="Email">
        <circle cx="12" cy="12" r="12" fill="#6a6a6a"/>
        <rect x="6" y="8" width="12" height="8" rx="1" fill="#1d1e20"/>
        <path d="M6.5 8.5 12 12.5l5.5-4" stroke="#6a6a6a" stroke-width="1" fill="none"/>
      </svg>
      <svg viewBox="0 0 24 24" aria-label="Website">
        <circle cx="12" cy="12" r="12" fill="#6a6a6a"/>
        <circle cx="12" cy="12" r="6" fill="none" stroke="#1d1e20" stroke-width="1.5"/>
        <ellipse cx="12" cy="12" rx="2.5" ry="6" fill="none" stroke="#1d1e20" stroke-width="1.2"/>
        <path d="M6 12h12" stroke="#1d1e20" stroke-width="1.2"/>
      </svg>
      <span class="rule"></span>
    </div>

    <div class="contact-list">
      <div>044-987 654 321</div>
      <div>hello@brightmesh.io</div>
      <div>www.brightmesh.io</div>
    </div>
    <div class="divider"></div>
    <div class="address">
      <div>18 Harbour Lane</div>
      <div>Northland, 30218</div>
    </div>
  </section>

  <section class="card card-back">
    <div class="back-pattern" role="img" aria-label="Faint repeating brand watermark pattern in soft grey"></div>
    <div class="back-brand">brightmesh</div>
  </section>
</body>
</html>
```